Velmora Flowers Florist Flyer

We are requiring a flyer that advertises and promotes our new business. We specialise in weddings and events but would also like to branch out to corporates and an online subscription. Our brand is feminine/romantic with a touch of elegance and luxury. Our main colour schemes are white, black, gold and pale pink. Instagram: Velmora_flowers and website www.velmoraflowers.com.au
Target Market(s)
brides to be, females
Industry/Entity Type
Florist
Font styles to use
Sans Serif
Script
Other font styles liked:
- The Carpenter
Colors
ffffff
000000
333333
Requirements
Must have
- Feminine/romantic feel, through use of theme colours and elegant font
- our contact details Ph: 0478215096
- email address: contactus@velmoraflowers.com.au
Nice to have
- a description of us willing to work with clients to create their dream wedding flowers. That we offer consultations and no obligation quotes.

```html
<!DOCTYPE html>
<html lang="en">
<head>
<meta charset="utf-8">
<title>Velmora Flowers – Weddings &amp; Events Flyer</title>
<link rel="stylesheet" href="https://fonts.googleapis.com/css2?family=Poppins:wght@300;400&display=swap">
<style>
  :root {
    --paper: #ffffff;
    --blush: #eca4ca;
    --butter: #fcdc8c;
    --charcoal: #333333;
    --ink: #111111;
    --gold: #e6b547;
    --rose-photo: #e9d8c8;
    --white-bouquet: #cfd4c6;
    --mixed-bouquet: #7d8a6e;
  }
  * { box-sizing: border-box; margin: 0; padding: 0; }
  html, body { width: 1200px; height: 846px; overflow: hidden; background: var(--paper); }
  body { font-family: "Poppins", sans-serif; }

  .flyer { position: relative; width: 1200px; height: 846px; background: var(--paper); }

  .photo { position: absolute; }
  .photo--roses {
    left: 0; top: 39px; width: 428px; height: 299px;
    background: linear-gradient(135deg, #cfc6bd 0%, var(--rose-photo) 45%, #f3e3d6 60%, #bdb8b4 100%);
  }
  .photo--white-bouquet {
    left: 436px; top: 39px; width: 324px; height: 299px;
    background: radial-gradient(circle at 50% 50%, #eef0e8 0%, var(--white-bouquet) 40%, #dcdcd8 75%);
  }
  .photo--mixed-bouquet {
    left: 767px; top: 39px; width: 433px; height: 588px;
    background: radial-gradient(circle at 45% 38%, #d8c9b5 0%, var(--mixed-bouquet) 35%, #4b5346 65%, #7c8278 100%);
  }

  .brand-panel {
    position: absolute; left: 0; top: 346px; width: 760px; height: 281px;
    background: var(--blush);
    display: flex; align-items: center; justify-content: center;
  }
  .brand-name {
    color: var(--paper); font-weight: 300; font-size: 64px;
    letter-spacing: 6px; text-transform: uppercase; white-space: nowrap;
  }

  .pitch {
    position: absolute; left: 0; top: 634px; width: 760px; height: 171px;
    background: var(--butter); color: var(--ink);
    padding: 36px 0 0 66px;
  }
  .pitch__heading { font-weight: 400; font-size: 27px; line-height: 1.2; margin-bottom: 20px; }
  .pitch__body { font-weight: 400; font-size: 18.5px; line-height: 1.3; max-width: 650px; }

  .contact {
    position: absolute; left: 767px; top: 634px; width: 433px; height: 171px;
    background: var(--charcoal); list-style: none;
    padding: 13px 46px 0 0;
    display: flex; flex-direction: column; align-items: flex-end; gap: 11px;
  }
  .contact__item {
    display: flex; align-items: center; gap: 10px;
    color: var(--paper); font-weight: 300; font-size: 18px; line-height: 28px;
  }
  .contact__icon { width: 28px; height: 28px; flex: none; }
</style>
</head>
<body>
<main class="flyer">
  <div class="photo photo--roses" role="img" aria-label="Bridal bouquet of blush and cream roses resting on a bed"></div>
  <div class="photo photo--white-bouquet" role="img" aria-label="Hand holding a white rose and greenery bouquet with trailing ivy"></div>
  <div class="photo photo--mixed-bouquet" role="img" aria-label="Florist holding a bouquet of red and white roses, anthurium and magnolia leaves"></div>

  <section class="brand-panel">
    <h1 class="brand-name">Velmora Flowers</h1>
  </section>

  <section class="pitch">
    <h2 class="pitch__heading">Looking for flowers for a Wedding or Event?</h2>
    <p class="pitch__body">We specialise in flowers for weddings and events.<br>No matter how big or small we’re here to create the best looking flowers just for you.</p>
  </section>

  <ul class="contact">
    <li class="contact__item">0478215096
      <svg class="contact__icon" viewBox="0 0 28 28" aria-hidden="true">
        <circle cx="14" cy="14" r="12.5" fill="none" stroke="var(--gold)" stroke-width="1.6"/>
        <path d="M10 8.5l2 -0.5 1.6 3.3-1.3 1.2c.7 1.6 1.9 2.8 3.4 3.5l1.2-1.3 3.2 1.6-.5 2c-4.8.4-9.9-4.7-9.6-9.8z" fill="var(--paper)"/>
      </svg>
    </li>
    <li class="contact__item">contactus@velmoraflowers.com.au
      <svg class="contact__icon" viewBox="0 0 28 28" aria-hidden="true">
        <circle cx="14" cy="14" r="12.5" fill="none" stroke="var(--gold)" stroke-width="1.6"/>
        <rect x="8" y="9.5" width="12" height="9" rx="1" fill="var(--paper)"/>
        <path d="M8.5 10l5.5 4.5 5.5-4.5" fill="none" stroke="var(--charcoal)" stroke-width="1.2"/>
      </svg>
    </li>
    <li class="contact__item">www.velmoraflowers.com.au
      <svg class="contact__icon" viewBox="0 0 28 28" aria-hidden="true">
        <circle cx="14" cy="14" r="12.5" fill="none" stroke="var(--gold)" stroke-width="1.6"/>
        <circle cx="14" cy="14" r="2.6" fill="none" stroke="var(--paper)" stroke-width="1.6"/>
        <path d="M16.6 11.5v3.6c0 1.4 2.4 1.4 2.4-1.1a5 5 0 1 0-2 4" fill="none" stroke="var(--paper)" stroke-width="1.6" stroke-linecap="round"/>
      </svg>
    </li>
    <li class="contact__item">Velmora_flowers
      <svg class="contact__icon" viewBox="0 0 28 28" aria-hidden="true">
        <circle cx="14" cy="14" r="12.5" fill="none" stroke="var(--gold)" stroke-width="1.6"/>
      </svg>
    </li>
  </ul>
</main>
</body>
</html>
```